Floorplan brochure design for rental company

We need a brochure designed for our rental company, Bramble Tor Commons.
We have two different categories that we need on this brochure: townhomes (primary) and mobile homes. Size and layout is up to you... choose what you think works best for the information being presented. However, please do not use an odd shape or size; do use a size and format that can be printed by qelvaprint.com.
Font and color choices are up to you. If needed, the fonts from the logo are Americana Extra Bold and BlackJack.
Industry/Entity Type
It Company
Requirements
Must have
- 1. logo and office address/contact information
2. floorplans and prices from attached documents
3. amenities from attached document
Should not have
- Please do not use our website, brambletor.com, as a basis for any design or color scheme decisions. We are working on a redesign of that website with our new logo (attached).

```html
<!DOCTYPE html>
<html lang="en">
<head>
<meta charset="utf-8">
<title>Bramble Tor Commons – Brochure</title>
<link href="https://fonts.googleapis.com/css2?family=Oswald:wght@400;600&family=Open+Sans:wght@600;700&family=Bungee&display=swap" rel="stylesheet">
<style>
:root{
  --green-dark:#17704a;
  --green-mid:#24904c;
  --green-light:#3aa548;
  --heading-green:#3e8f2c;
  --accent-cyan:#1aa3c9;
  --paper:#ffffff;
  --plan-line:#8fd3e6;
}
*{box-sizing:border-box;margin:0;padding:0}
html,body{width:1200px;height:900px;overflow:hidden;background:var(--paper)}
body{position:relative;font-family:"Open Sans",sans-serif}
.abs{position:absolute}

/* front cover */
.cover{left:250px;top:25px;width:580px;height:380px;
  background:linear-gradient(180deg,var(--green-dark) 0%,#1a7a4b 60%,var(--green-light) 100%);overflow:hidden}
.cover-texture{position:absolute;inset:0;background:linear-gradient(120deg,rgba(255,255,255,.05),rgba(255,255,255,0) 50%,rgba(255,255,255,.06))}
.contact{left:100px;top:165px;width:180px;text-align:center;color:#fff;font-family:"Oswald",sans-serif;font-size:12px;line-height:15px}
.contact svg{vertical-align:-1px;margin-right:3px}
.brand{left:318px;top:222px;width:210px;text-align:center}
.brand-dot{width:22px;height:22px;border-radius:50%;background:var(--accent-cyan);margin:0 auto 8px}
.brand-name{font-family:"Oswald",sans-serif;font-weight:600;font-size:28px;line-height:32px;color:#6fbf3a}

.side-label{font-family:"Bungee",sans-serif;color:var(--accent-cyan);font-size:22px;letter-spacing:1px}

/* back spread */
.back{left:255px;top:455px;width:575px;height:383px;overflow:hidden}
.panel-left{left:0;top:0;width:228px;height:383px;background:linear-gradient(180deg,var(--green-mid),var(--green-dark) 80%,#166a40)}
.panel-right{left:342px;top:0;width:233px;height:383px;background:linear-gradient(180deg,var(--green-mid),var(--green-dark) 80%,#166a40)}
.panel-mid-bg{left:228px;top:0;width:114px;height:383px;background:linear-gradient(180deg,var(--green-light),var(--green-mid))}
.section-title{font-family:"Oswald",sans-serif;font-weight:400;color:#fff;font-size:26px;line-height:30px;white-space:nowrap}
.card{background:var(--paper);border-radius:0 12px 12px 0}
.card.right{border-radius:12px 0 0 12px}
.plan-title{font-family:"Oswald",sans-serif;font-weight:600;color:var(--heading-green);font-size:13px;line-height:17px;white-space:nowrap}
.plan-list{list-style:none;font-size:6.5px;line-height:8px;color:var(--accent-cyan);font-weight:700;white-space:nowrap}
.plan-list li::before{content:"";display:inline-block;width:4px;height:4px;background:var(--heading-green);margin-right:2px;vertical-align:1px}
.price{font-family:"Oswald",sans-serif;font-weight:600;color:var(--heading-green);font-size:15px;line-height:18px;white-space:nowrap}
.align-right{text-align:right}
.plan-drawing{background:#eef9fc;border:1px solid var(--plan-line)}
.note{font-size:4.5px;letter-spacing:.6px;color:#e6f4ea;white-space:nowrap}

.mid-panel{left:230px;top:50px;width:110px;height:333px;background:var(--paper);border-radius:10px 10px 0 0;padding:6px 4px}
.mid-panel h3{font-family:"Oswald",sans-serif;font-weight:600;color:var(--heading-green);font-size:11px;margin:0 0 4px}
.amen-list{list-style:none;font-size:4.6px;line-height:6.6px;color:var(--accent-cyan);font-weight:700}
.amen-list li::before{content:"";display:inline-block;width:3px;height:3px;background:var(--heading-green);margin-right:2px}
.footnote{font-size:4.5px;color:var(--accent-cyan);font-weight:700;white-space:nowrap}
</style>
</head>
<body>

<!-- front cover -->
<section class="abs cover">
  <div class="cover-texture" role="img" aria-label="Faint floor plan pattern across the cover"></div>
  <div class="abs contact">
    <div><svg width="8" height="9" viewBox="0 0 8 9"><path d="M2 0 L3.5 2.5 L2.5 3.5 Q3.5 5.5 5 6.5 L6 5.5 L8 7 L6.5 9 Q1 7 0 1.5 Z" fill="#fff"/></svg>555-214-0382</div>
    <div>www.brambletor.com</div>
    <div>418 Wrenfield Ave.</div>
    <div>Harlow Bend TX, 75012</div>
  </div>
  <div class="abs brand">
    <div class="brand-dot"></div>
    <div class="brand-name">Bramble Tor Commons</div>
  </div>
</section>
<div class="abs side-label" style="left:528px;top:420px">front</div>

<!-- back spread -->
<section class="abs back">
  <div class="abs panel-left"></div>
  <div class="abs panel-mid-bg"></div>
  <div class="abs panel-right"></div>

  <h2 class="abs section-title" style="left:10px;top:11px">town houses</h2>
  <h2 class="abs section-title" style="left:237px;top:22px;font-size:24px">amenities</h2>
  <h2 class="abs section-title" style="right:13px;top:11px">motor homes</h2>

  <!-- town house cards -->
  <div class="abs card" style="left:0;top:38px;width:206px;height:98px">
    <div class="abs plan-title" style="left:13px;top:6px">Plan 1272<br>&nbsp;Includes:</div>
    <ul class="abs plan-list" style="left:10px;top:40px"><li>2 bedrooms</li><li>2.5 Bathrooms</li><li>2 Story</li></ul>
    <div class="abs price" style="left:10px;top:64px">$925</div>
    <div class="abs plan-drawing" role="img" aria-label="Two-story floor plan for plan 1272" style="left:72px;top:3px;width:130px;height:90px"></div>
  </div>
  <div class="abs card" style="left:0;top:143px;width:206px;height:97px">
    <div class="abs plan-drawing" role="img" aria-label="Two-story floor plan for plan 1132" style="left:6px;top:4px;width:125px;height:88px"></div>
    <div class="abs plan-title align-right" style="right:8px;top:6px">Plan 1132<br>Includes:</div>
    <ul class="abs plan-list align-right" style="right:8px;top:39px"><li>2 bedrooms</li><li>2.5 Bathrooms</li><li>2 Story</li></ul>
    <div class="abs price" style="right:8px;top:64px">$875</div>
  </div>
  <div class="abs card" style="left:0;top:248px;width:206px;height:112px">
    <div class="abs plan-drawing" role="img" aria-label="Single-story floor plan for plans 1069 and 1070" style="left:6px;top:5px;width:80px;height:100px"></div>
    <div class="abs plan-title" style="left:95px;top:15px">Plan 1069<br>&nbsp;Includes:</div>
    <ul class="abs plan-list" style="left:92px;top:48px"><li>2 bedrooms</li><li>2 Bathrooms</li><li>1 Story</li></ul>
    <div class="abs price" style="left:93px;top:76px">$900</div>
    <div class="abs plan-title" style="left:150px;top:15px">Plan 1070<br>&nbsp;Includes:</div>
    <ul class="abs plan-list" style="left:147px;top:48px"><li>2 bedrooms</li><li>2 Bathrooms</li><li>1 Story</li><li>Covered Patio</li></ul>
    <div class="abs price" style="left:148px;top:80px">$925</div>
  </div>
  <div class="abs note" style="left:10px;top:364px">PRICE SUBJECT TO CHANGE WITHOUT NOTICE</div>

  <!-- amenities -->
  <div class="abs mid-panel">
    <ul class="amen-list">
      <li>Overall Features</li><li>Golf course</li><li>Convenience Store</li><li>Gated Access</li><li>Playground</li><li>Basketball Court</li><li>Stocked fishing lake</li><li>Pet Friendly*</li><li>Dog Park</li><li>Extra storage available</li><li>Lawn care included</li><li>Outdoor grills permitted</li>
    </ul>
    <div class="footnote" style="margin:8px 0 0 2px">*Breed restrictions</div>
    <h3 style="margin-top:38px">All units offer:</h3>
    <ul class="amen-list">
      <li>Fenced back yards with concrete patio</li><li>Assigned front door parking</li><li>Ceiling fans in every room</li><li>Dishwasher, microwaves, refrigerator &amp; range</li><li>Full-size washer and dryer connections</li>
    </ul>
    <h3 style="margin-top:14px">For Town Houses:</h3>
    <ul class="amen-list">
      <li>6 foot privacy fenced backyard.</li><li>Concrete backyard patio.</li><li>Assigned front door parking.</li>
    </ul>
    <h3 style="margin-top:8px">For Mobile Homes:</h3>
    <ul class="amen-list">
      <li>Large fenced backyards.</li><li>Concrete patio.</li><li>Private driveway.</li>
    </ul>
  </div>

  <!-- motor home cards -->
  <div class="abs card right" style="left:365px;top:38px;width:210px;height:97px">
    <div class="abs plan-drawing" role="img" aria-label="Floor plan for plan 1648" style="left:5px;top:20px;width:142px;height:38px"></div>
    <div class="abs plan-title align-right" style="right:12px;top:8px">Plan 1648<br>Includes:</div>
    <ul class="abs plan-list align-right" style="right:12px;top:42px"><li>16' x 52'</li><li>2 Bedrooms</li><li>1 Bathrooms</li></ul>
    <div class="abs price" style="right:12px;top:68px">$750</div>
  </div>
  <div class="abs card right" style="left:365px;top:143px;width:210px;height:95px">
    <div class="abs plan-title" style="left:10px;top:6px">Plan 2762<br>&nbsp;Includes:</div>
    <ul class="abs plan-list" style="left:6px;top:40px"><li>16' x 76'</li><li>3 Bedrooms</li><li>2 Bathrooms</li></ul>
    <div class="abs price" style="left:6px;top:66px">$850</div>
    <div class="abs plan-drawing" role="img" aria-label="Floor plan for plan 2762" style="left:70px;top:32px;width:134px;height:32px"></div>
  </div>
  <div class="abs card right" style="left:365px;top:253px;width:210px;height:93px">
    <div class="abs plan-drawing" role="img" aria-label="Floor plan for plan 1887" style="left:12px;top:24px;width:118px;height:32px"></div>
    <div class="abs plan-title align-right" style="right:12px;top:1px">Plan 1887<br>Includes:</div>
    <ul class="abs plan-list align-right" style="right:12px;top:34px"><li>16' x 76'</li><li>3 Bedrooms</li><li>2 Bathrooms</li></ul>
    <div class="abs price" style="right:10px;top:58px">$750 or $950*</div>
    <div class="abs footnote" style="right:12px;top:80px">*With 8' x 8' Storage Building</div>
  </div>
  <div class="abs note" style="right:10px;top:364px">PRICE SUBJECT TO CHANGE WITHOUT NOTICE</div>
</section>
<div class="abs side-label" style="left:532px;top:845px">back</div>

</body>
</html>
```